Letterhead

We are looking for a basic letterhead. It should include our logo, website - northpeakkitchenware.com, phone 907.418.3952, toll free 855.392.6180, and fax 907.418.5263, along with our address 4837 Birchwood Lane, Anchorage, AK 99517. I want something that will look good printed in color or black and white.

```html
<!DOCTYPE html>
<html lang="en">
<head>
<meta charset="utf-8">
<title>North Peak Kitchenware — Letterhead</title>
<link rel="stylesheet" href="https://fonts.googleapis.com/css2?family=Arimo:wght@400;700&display=swap">
<style>
  :root {
    --backdrop: #e9eaec;
    --paper: #ffffff;
    --brand-blue: #1669d8;
    --brand-pink: #d1306c;
    --rule: #d9dbde;
    --icon-grey: #a3a7ad;
  }
  * { box-sizing: border-box; margin: 0; padding: 0; }
  html, body {
    width: 1200px;
    height: 1200px;
    overflow: hidden;
    background: var(--backdrop);
    font-family: "Arimo", Arial, sans-serif;
  }
  .letterhead {
    position: absolute;
    left: 175px;
    top: 50px;
    width: 850px;
    height: 1100px;
    background: var(--paper);
    box-shadow: 0 2px 10px rgba(0,0,0,0.12);
  }
  .letterhead-header {
    position: absolute;
    left: 56px;
    top: 62px;
    right: 56px;
    display: flex;
    align-items: flex-start;
  }
  .brand {
    width: 250px;
    display: flex;
    align-items: center;
    gap: 10px;
    padding-top: 18px;
  }
  .brand-mark {
    width: 16px;
    height: 16px;
    background: var(--brand-blue);
    flex: none;
  }
  .brand-name {
    font-weight: 700;
    font-size: 22px;
    line-height: 1.1;
    color: var(--brand-blue);
  }
  .header-rule {
    width: 1px;
    height: 82px;
    background: var(--rule);
    margin: 0 26px 0 18px;
  }
  .contact-list {
    list-style: none;
    display: grid;
    grid-template-columns: 18px 78px 1fr;
    row-gap: 6px;
    align-items: center;
    font-size: 13.5px;
    padding-top: 6px;
  }
  .contact-list li { display: contents; }
  .contact-icon { width: 12px; height: 12px; fill: var(--icon-grey); }
  .contact-label { color: var(--brand-pink); }
  .contact-value { color: var(--brand-blue); }
  .contact-value::before { content: ":  "; white-space: pre; }
</style>
</head>
<body>
  <main class="letterhead">
    <header class="letterhead-header">
      <div class="brand">
        <span class="brand-mark"></span>
        <span class="brand-name">North Peak Kitchenware</span>
      </div>
      <div class="header-rule"></div>
      <ul class="contact-list">
        <li>
          <svg class="contact-icon" viewBox="0 0 12 12" aria-hidden="true"><path d="M2.5 0.5l2 2.4-1.1 1.3c.7 1.6 2 2.9 3.4 3.5l1.3-1.1 2.4 2-1.3 2C5 10.3 1.6 7 .6 1.8z"/></svg>
          <span class="contact-label">Phone</span>
          <span class="contact-value">907.418.3952 , 855.392.6180 (Toll Free)</span>
        </li>
        <li>
          <svg class="contact-icon" viewBox="0 0 12 12" aria-hidden="true"><path d="M3 0h6v3H3zM1 4h10v5H9.5v3h-7V9H1zM3.5 8v3h5V8z"/></svg>
          <span class="contact-label">Fax</span>
          <span class="contact-value">907.418.5263</span>
        </li>
        <li>
          <svg class="contact-icon" viewBox="0 0 12 12" aria-hidden="true"><path d="M6 0a4 4 0 0 1 4 4c0 3-4 8-4 8S2 7 2 4a4 4 0 0 1 4-4zm0 2.4a1.6 1.6 0 1 0 0 3.2 1.6 1.6 0 0 0 0-3.2z"/></svg>
          <span class="contact-label">Address</span>
          <span class="contact-value">4837 Birchwood Lane, Anchorage, AK 99517</span>
        </li>
        <li>
          <svg class="contact-icon" viewBox="0 0 12 12" aria-hidden="true"><path d="M2 0l8 6-3.4.6 2 4.3-1.6.8-2-4.3L2 10z"/></svg>
          <span class="contact-label">Website</span>
          <span class="contact-value">www.northpeakkitchenware.com</span>
        </li>
      </ul>
    </header>
  </main>
</body>
</html>
```